Esthetically Pleasing Core Values and Brand Promise for Accounting Firm

I would like a cohesive design that ties together my core values and brand promise. My firm, Maple Finch Advisory, provides accounting work to small businesses. I prefer modern and clean designs. I want my Core Values and Brand Promise to represent me - sole entrepreneur, married, mother of two kids, modern esthetics, clean lines, organized, colorful (teals, greys, white, yellows)

Industry/Entity Type

Public Accounting

Colors
33b8a4

```html
<!DOCTYPE html>
<html lang="en">
<head>
<meta charset="UTF-8">
<title>Maple Finch Advisory – Flyer</title>
<link href="https://fonts.googleapis.com/css2?family=Montserrat:wght@300;400;500;700;800&display=swap" rel="stylesheet">
<style>
  :root {
    --teal: #33b8a4;
    --teal-deep: #11a596;
    --teal-dark: #0b5e5a;
    --yellow: #f3e04a;
    --ink: #4a4a4a;
    --ink-soft: #6b6b6b;
    --paper: #ffffff;
    --backdrop: #e9e9e9;
  }
  * { box-sizing: border-box; margin: 0; padding: 0; }
  html, body { width: 1200px; height: 857px; overflow: hidden; }
  body {
    background: var(--backdrop);
    font-family: "Montserrat", sans-serif;
    color: var(--ink);
  }
  .flyer {
    position: absolute;
    left: 300px; top: 18px;
    width: 600px; height: 821px;
    background: var(--paper);
    box-shadow: 0 6px 20px rgba(0,0,0,.12);
    overflow: hidden;
  }
  .header { position: relative; height: 165px; }
  .brand {
    position: absolute; left: 36px; top: 92px;
    display: flex; align-items: center; gap: 10px;
    font-weight: 500; font-size: 30px; color: var(--teal-deep);
    letter-spacing: 1px;
  }
  .brand-dot { width: 22px; height: 22px; border-radius: 50%; background: var(--teal-deep); }
  .intro { position: absolute; right: 34px; top: 26px; width: 290px; text-align: right; }
  .intro-title {
    font-weight: 400; font-size: 28px; letter-spacing: 3px;
    color: var(--teal-deep); text-transform: uppercase;
  }
  .intro-text { margin-top: 6px; font-size: 8.5px; line-height: 1.45; color: var(--ink-soft); }

  .hero { position: relative; height: 225px; }
  .hero-image {
    position: absolute; inset: 0;
    background:
      radial-gradient(ellipse at 30% 40%, rgba(80,210,190,.55), transparent 60%),
      linear-gradient(120deg, #0c5d5a 0%, #159a8e 45%, #1fb3a2 70%, #0f7470 100%);
  }
  .hero-headline {
    position: absolute; right: 40px; top: 58px;
    color: var(--yellow); font-weight: 800; font-size: 29px; line-height: 1.15;
  }
  .hero-headline .light { font-weight: 400; }

  .services { display: flex; justify-content: space-between; padding: 32px 40px 0; height: 150px; }
  .service { width: 240px; text-align: center; }
  .service-title {
    font-weight: 700; font-size: 11px; letter-spacing: .5px; text-transform: uppercase; color: #333;
  }
  .service-title::after {
    content: ""; display: block; width: 22px; height: 2px;
    background: var(--teal); margin: 5px auto 10px;
  }
  .service-text { font-size: 11.5px; line-height: 1.4; color: var(--ink-soft); }

  .values { background: var(--teal-deep); height: 175px; padding: 20px 26px 0; }
  .values-title { text-align: center; color: var(--yellow); font-weight: 700; font-size: 22px; margin-bottom: 16px; }
  .values-grid { display: flex; justify-content: space-between; }
  .value { width: 128px; text-align: center; color: var(--paper); }
  .value-name { font-weight: 700; font-size: 10.5px; text-transform: uppercase; margin-bottom: 4px; }
  .value-text { font-size: 10px; line-height: 1.4; font-weight: 400; }

  .contact { display: flex; justify-content: space-between; align-items: flex-end; padding: 40px 40px 0; }
  .contact-item { display: flex; flex-direction: column; align-items: center; gap: 8px; font-size: 10.5px; color: var(--ink-soft); }
  .contact-item svg { fill: #555; }
</style>
</head>
<body>
  <article class="flyer">
    <header class="header">
      <div class="brand"><span class="brand-dot"></span>Maple Finch</div>
      <div class="intro">
        <h1 class="intro-title">Advisory</h1>
        <p class="intro-text">Maple Finch Advisory is an Orange County based company that handles accounting services for all types of individuals and businesses. Our staff has been working in the public accounting industry for over 14 years and has a wide range of knowledge on all matters.</p>
      </div>
    </header>

    <section class="hero">
      <div class="hero-image" role="img" aria-label="Teal-toned financial bar charts, line graphs and market figures"></div>
      <h2 class="hero-headline">Trust,<br>Transparency <span class="light">and</span><br>Dependability</h2>
    </section>

    <section class="services">
      <div class="service">
        <h3 class="service-title">Tax</h3>
        <p class="service-text">Maple Finch provides all clients with a trusted tax advisor who provides accuracy in all filings and ensures your compliance with all government agencies.</p>
      </div>
      <div class="service">
        <h3 class="service-title">Accounting</h3>
        <p class="service-text">Maple Finch provides all business owners with the financial visibility needed to foster growth and facilitate goals.</p>
      </div>
    </section>

    <section class="values">
      <h2 class="values-title">Core Values</h2>
      <div class="values-grid">
        <div class="value"><h4 class="value-name">Empower</h4><p class="value-text">We are dedicated, appreciative and respectful of people's time and purpose.</p></div>
        <div class="value"><h4 class="value-name">Client Focused</h4><p class="value-text">We provide a personal service that goes above the standards of professional care.</p></div>
        <div class="value"><h4 class="value-name">Rectitude</h4><p class="value-text">We know the difference between what we have the right to do and what the right thing to do</p></div>
        <div class="value"><h4 class="value-name">Relentless</h4><p class="value-text">We believe that the longer we try to do our best, the better we become.</p></div>
      </div>
    </section>

    <footer class="contact">
      <div class="contact-item">
        <svg width="16" height="16" viewBox="0 0 24 24" aria-hidden="true"><path d="M6.6 10.8a15.1 15.1 0 0 0 6.6 6.6l2.2-2.2a1 1 0 0 1 1-.25 11.4 11.4 0 0 0 3.6.57 1 1 0 0 1 1 1V20a1 1 0 0 1-1 1A17 17 0 0 1 3 4a1 1 0 0 1 1-1h3.5a1 1 0 0 1 1 1c0 1.25.2 2.45.57 3.57a1 1 0 0 1-.25 1z"/></svg>
        <span>555.014.2290</span>
      </div>
      <div class="contact-item">
        <svg width="16" height="20" viewBox="0 0 24 30" aria-hidden="true"><path d="M12 0A11 11 0 0 0 1 11c0 8 11 19 11 19s11-11 11-19A11 11 0 0 0 12 0zm0 15a4 4 0 1 1 0-8 4 4 0 0 1 0 8z"/></svg>
        <span>1150 W. Linden Court, Suite 300 Fairview, CA 92700</span>
      </div>
    </footer>
  </article>
</body>
</html>
```